Kettlecrown Premium Lager beer labels

Design a beer bottle label for Kettlecrown Premium Lager. The beer is brewed and aged in the Williams Fork River in Colorado. The label should use the KV/antler logo and design. The label will be used on a long neck bottle so it will require a neck label (simple logo only). The beer company was established in 2020.

Target Market(s)

Consumers 21-45

Industry/Entity Type

Beverages

Requirements
Must have
• KC Logo
Should not have
• White label

```html
<!DOCTYPE html>
<html lang="en">
<head>
<meta charset="utf-8">
<title>Kettlecrown Premium Lager – Neck and Body Labels</title>
<link rel="stylesheet" href="https://fonts.googleapis.com/css2?family=Oswald:wght@500;600&display=swap">
<style>
  :root {
    --backdrop: #d6f7fc;
    --label-blue: #1b2c80;
    --label-blue-light: #24378f;
    --ranch-red: #e84545;
    --ink-white: #ffffff;
    --edge: #5a6480;
  }
  html, body {
    margin: 0;
    padding: 0;
    width: 1200px;
    height: 769px;
    overflow: hidden;
    background: var(--backdrop);
    font-family: "Oswald", "Arial Narrow", sans-serif;
  }
  .canvas {
    position: relative;
    width: 1200px;
    height: 769px;
  }

  /* shared label parts */
  .label {
    position: absolute;
    background: var(--label-blue);
    outline: 1px solid var(--edge);
    overflow: hidden;
    color: var(--ink-white);
  }
  .brand-block {
    position: absolute;
    left: 0;
    width: 100%;
    text-align: center;
  }
  .brand-initials {
    display: block;
    font-weight: 600;
    line-height: 1;
    letter-spacing: 2px;
  }
  .brand-name {
    display: block;
    font-weight: 600;
    line-height: 1;
    letter-spacing: 1px;
  }
  .brand-sub {
    display: inline-flex;
    align-items: center;
    gap: 6px;
    font-weight: 600;
    letter-spacing: 1px;
    line-height: 1;
  }
  .brand-sub::before,
  .brand-sub::after {
    content: "";
    height: 2px;
    background: var(--ink-white);
  }

  /* neck label */
  .neck-label {
    left: 230px;
    top: 254px;
    width: 200px;
    height: 260px;
  }
  .neck-label .brand-block { top: 58px; }
  .neck-label .brand-initials { font-size: 60px; }
  .neck-label .brand-name { font-size: 26px; margin-top: 18px; }
  .neck-label .brand-sub { font-size: 11px; margin-top: 6px; }
  .neck-label .brand-sub::before,
  .neck-label .brand-sub::after { width: 52px; }

  /* body label */
  .body-label {
    left: 540px;
    top: 144px;
    width: 480px;
    height: 480px;
  }
  .top-rule {
    position: absolute;
    left: 0;
    top: 23px;
    width: 100%;
    height: 4px;
    background: var(--ranch-red);
  }
  .mountain-scene {
    position: absolute;
    left: 0;
    top: 183px;
    width: 100%;
    height: 252px;
    background: linear-gradient(180deg, rgba(36,55,143,0) 0%, var(--label-blue-light) 50%, #22348a 100%);
  }
  .body-label .brand-block { top: 48px; }
  .body-label .brand-initials { font-size: 72px; }
  .body-label .brand-name { font-size: 30px; margin-top: 14px; }
  .body-label .brand-sub { font-size: 13px; margin-top: 6px; }
  .body-label .brand-sub::before,
  .body-label .brand-sub::after { width: 70px; }

  .beer-title {
    position: absolute;
    left: 0;
    top: 242px;
    width: 100%;
    margin: 0;
    text-align: center;
    font-weight: 600;
    font-size: 46px;
    line-height: 44px;
    letter-spacing: 1px;
  }
  .volume {
    position: absolute;
    right: 89px;
    top: 396px;
    font-weight: 500;
    font-size: 18px;
    line-height: 1;
    letter-spacing: 2px;
  }
  .origin-band {
    position: absolute;
    left: 0;
    bottom: 0;
    width: 100%;
    height: 46px;
    background: var(--ranch-red);
    display: flex;
    align-items: center;
    justify-content: center;
    text-align: center;
    font-weight: 500;
    font-size: 10px;
    line-height: 11px;
    letter-spacing: 0.8px;
  }
</style>
</head>
<body>
<main class="canvas">
  <section class="label neck-label" aria-label="Neck label">
    <div class="brand-block">
      <span class="brand-initials">KC</span>
      <span class="brand-name">KETTLECROWN</span>
      <span class="brand-sub">RANCH</span>
    </div>
  </section>

  <section class="label body-label" aria-label="Body label">
    <div class="top-rule"></div>
    <div class="mountain-scene" role="img" aria-label="Faint engraved mountain peak with pine forest in label blue"></div>
    <div class="brand-block">
      <span class="brand-initials">KC</span>
      <span class="brand-name">KETTLECROWN</span>
      <span class="brand-sub">RANCH</span>
    </div>
    <h1 class="beer-title">PREMIUM RANCH<br>LAGER</h1>
    <div class="volume">350ML</div>
    <div class="origin-band">WILLIANS FORK MOUNTAINS<br>COLORADO</div>
  </section>
</main>
</body>
</html>
```